Create a Professional PowerPoint Slide Deck

I need a professional looking and editable PowerPoint presentation with contents based on the attached PDF.

I would like to see the following;
- add design elements to every slide (cover, title, contents etc)
- enhance the graphs or charts
- same copy will be used
I'm attaching the document to be put into powerpoint (KWRO white paper: "Cargo Wise")

Target Market(s)

Executives and managers responsible for the distribution of products

Industry/Entity Type

It Professional

Font styles to use
Serif

Colors

Designer to choose colors to be used in the design.

Requirements
Must have
• The format should be portrait orientation as this may be printed on paper and converted to PDF for distribution
• Complete conversion of all pages in the attached White Paper
• Upgraded graphics and formatting
Nice to have
• Any creative ideas to make the presentation more attractive or easier to understand
• Color scheme should complement the KWRO Freightlines Logo (red and black)

```html
<!DOCTYPE html>
<html lang="en">
<head>
<meta charset="utf-8">
<title>A Better Way to Handle Multiple Quotes – KWRO Freightlines</title>
<link href="https://fonts.googleapis.com/css2?family=Roboto:ital,wght@0,300;0,400;0,700;0,900;1,700&display=swap" rel="stylesheet">
<style>
  :root{
    --ink:#1b1b1b;
    --black:#141414;
    --red:#e4191f;
    --body:#2a2a2a;
    --paper:#ffffff;
    --canvas:#ffffff;
    --grid:#cfcfcf;
    --cell:#333333;
  }
  *{box-sizing:border-box;margin:0;padding:0}
  html,body{width:1200px;height:848px;overflow:hidden;background:var(--canvas)}
  body{position:relative;font-family:"Roboto",Arial,sans-serif}

  .page{
    position:absolute;left:369px;top:84px;width:462px;height:616px;
    background:var(--paper);
    box-shadow:3px 6px 8px rgba(0,0,0,.45);
  }

  .title-block{position:absolute;left:0;top:0;width:270px;height:58px}
  .title-block svg{position:absolute;left:0;top:0}
  .title-kicker{
    position:absolute;left:28px;top:4px;
    color:#fff;font-weight:700;font-size:18.5px;letter-spacing:-.2px;line-height:22px;
  }
  .title-main{
    position:absolute;left:28px;top:29px;
    color:#fff;font-weight:900;font-size:23px;letter-spacing:-.4px;line-height:28px;
  }

  .content{
    position:absolute;left:24px;top:68px;width:409px;
    color:var(--body);font-weight:300;font-size:15px;line-height:19.2px;
    text-align:justify;
  }

  .data-figure{
    float:right;width:262px;height:348px;margin:0 0 0 12px;padding-top:0;
  }
  .sheet{
    width:261px;height:218px;background:#fff;overflow:hidden;
    box-shadow:2px 3px 5px rgba(0,0,0,.45);
    padding:2px 3px;
  }
  .sheet table{border-collapse:collapse;width:100%;font-family:"Roboto",Arial,sans-serif;font-weight:400;font-size:3.4px;line-height:5.2px;color:var(--cell);text-align:left}
  .sheet th{font-weight:400;font-size:3.6px;border-bottom:.4px solid var(--grid);white-space:nowrap}
  .sheet td{white-space:nowrap;border-bottom:.3px solid #ececec}
  .sheet td.num{text-align:right}
  .figure-caption{
    margin-top:12px;text-align:center;color:var(--red);
    font-style:italic;font-weight:400;font-size:12px;line-height:14px;
  }

  .section-heading{
    color:var(--red);font-style:italic;font-weight:700;font-size:18px;line-height:22px;
    text-align:left;margin-top:6px;margin-bottom:28px;
  }
  .content p{margin-bottom:19px}
</style>
</head>
<body>
  <article class="page">
    <header class="title-block">
      <svg width="270" height="58" viewBox="0 0 270 58" aria-hidden="true">
        <polygon points="0,0 266,0 248,28 0,28" fill="var(--black)"/>
        <polygon points="0,28 229,28 210,58 0,58" fill="var(--red)"/>
      </svg>
      <div class="title-kicker">A Better Way to Handle</div>
      <h1 class="title-main">Multiple Quotes</h1>
    </header>

    <section class="content">
      <figure class="data-figure">
        <div class="sheet">
          <table>
            <thead>
              <tr><th>Client</th><th>Household</th><th>Shipment Date</th><th>Scac</th><th>Consignee Name</th><th>Consignee Zi</th><th>Shipper Zip</th><th>Status</th><th>Chargeable's Invoice Total</th></tr>
            </thead>
            <tbody>
              <tr><td>Brightline Parts</td><td>9947814</td><td>2/12/16 13:00</td><td>LT</td><td>AAA</td><td class="num">89040</td><td>85043</td><td>CAN</td><td class="num">875</td></tr>
              <tr><td>Brightline Parts</td><td>9956135</td><td>3/31/16 13:00</td><td>LT</td><td>BBB</td><td class="num">89040</td><td>90280</td><td>CAN</td><td class="num">730</td></tr>
              <tr><td>Brightline Parts</td><td>9963081</td><td>5/18/16 13:00</td><td>LT</td><td>CCC</td><td class="num">7724</td><td>85043</td><td>CAN</td><td class="num">557</td></tr>
              <tr><td>Brightline Parts</td><td>9969571</td><td>6/22/16 13:00</td><td>LT</td><td>DDD</td><td class="num">90027</td><td>85043</td><td>CAN</td><td class="num">258</td></tr>
              <tr><td>Brightline Parts</td><td>1224144</td><td>7/18/16 13:00</td><td>LT</td><td>EEE</td><td class="num">76106</td><td>85043</td><td>CAN</td><td class="num">303</td></tr>
              <tr><td>Brightline Parts</td><td>1225322</td><td>7/22/16 13:00</td><td>LT</td><td>FFF</td><td class="num">89130</td><td>85043</td><td>CAN</td><td class="num">284</td></tr>
              <tr><td>Brightline Parts</td><td>1226460</td><td>8/15/16 13:00</td><td>LT</td><td>AAA</td><td class="num">40408</td><td>85043</td><td>CAN</td><td class="num">405</td></tr>
              <tr><td>Brightline Parts</td><td>1227405</td><td>8/5/16 13:00</td><td>LT</td><td>BBB</td><td class="num">93126</td><td>85043</td><td>DEL</td><td class="num">179.94</td></tr>
              <tr><td>Brightline Parts</td><td>1228719</td><td>8/22/16 13:00</td><td>LT</td><td>CCC</td><td class="num">53075</td><td>85043</td><td>DEL</td><td class="num">191.57</td></tr>
              <tr><td>Brightline Parts</td><td>1239899</td><td>8/24/16 13:00</td><td>LT</td><td>DDD</td><td class="num">37564</td><td>85043</td><td>DEL</td><td class="num">229.90</td></tr>
              <tr><td>Brightline Parts</td><td>1240615</td><td>8/25/16 13:00</td><td>LT</td><td>EEE</td><td class="num">87022</td><td>85043</td><td>DEL</td><td class="num">119.11</td></tr>
              <tr><td>Brightline Parts</td><td>1240642</td><td>8/26/16 13:00</td><td>LT</td><td>FFF</td><td class="num">7724</td><td>85043</td><td>DEL</td><td class="num">408.44</td></tr>
              <tr><td>Brightline Parts</td><td>1240647</td><td>8/26/16 13:00</td><td>LT</td><td>AAA</td><td class="num">40601</td><td>85043</td><td>DEL</td><td class="num">141.83</td></tr>
              <tr><td>Brightline Parts</td><td>1240778</td><td>8/29/16 13:00</td><td>LT</td><td>BBB</td><td class="num">39132</td><td>85043</td><td>DEL</td><td class="num">183.74</td></tr>
              <tr><td>Brightline Parts</td><td>1241113</td><td>8/31/16 13:00</td><td>LT</td><td>CCC</td><td class="num">37421</td><td>85043</td><td>DEL</td><td class="num">548.07</td></tr>
              <tr><td>Brightline Parts</td><td>1241140</td><td>8/31/16 13:00</td><td>LT</td><td>DDD</td><td class="num">53821</td><td>85043</td><td>DEL</td><td class="num">132.40</td></tr>
              <tr><td>Brightline Parts</td><td>1241152</td><td>8/31/16 13:00</td><td>LT</td><td>EEE</td><td class="num">76106</td><td>85043</td><td>DEL</td><td class="num">325.84</td></tr>
              <tr><td>Brightline Parts</td><td>1241163</td><td>8/31/16 13:00</td><td>LT</td><td>FFF</td><td class="num">71110</td><td>85043</td><td>DEL</td><td class="num">610</td></tr>
              <tr><td>Brightline Parts</td><td>1241180</td><td>8/31/16 13:00</td><td>LT</td><td>AAA</td><td class="num">40351</td><td>85043</td><td>DEL</td><td class="num">247.2</td></tr>
              <tr><td>Brightline Parts</td><td>1241222</td><td>8/31/16 13:00</td><td>LT</td><td>BBB</td><td class="num">41059</td><td>85043</td><td>DEL</td><td class="num">143.79</td></tr>
              <tr><td>Brightline Parts</td><td>1241331</td><td>9/1/16 13:00</td><td>LT</td><td>CCC</td><td class="num">60502</td><td>85043</td><td>DEL</td><td class="num">131.47</td></tr>
              <tr><td>Brightline Parts</td><td>1241348</td><td>9/1/16 13:00</td><td>LT</td><td>DDD</td><td class="num">91701</td><td>85043</td><td>DEL</td><td class="num">123.67</td></tr>
              <tr><td>Brightline Parts</td><td>1241359</td><td>9/1/16 13:00</td><td>LT</td><td>EEE</td><td class="num">89502</td><td>85043</td><td>DEL</td><td class="num">128.77</td></tr>
              <tr><td>Brightline Parts</td><td>1241383</td><td>9/1/16 13:00</td><td>LT</td><td>FFF</td><td class="num">81286</td><td>85043</td><td>DEL</td><td class="num">131.37</td></tr>
              <tr><td>Brightline Parts</td><td>1241385</td><td>9/1/16 13:00</td><td>LT</td><td>AAA</td><td class="num">84651</td><td>85043</td><td>DEL</td><td class="num">125.97</td></tr>
              <tr><td>Brightline Parts</td><td>1241640</td><td>9/5/16 13:00</td><td>LT</td><td>BBB</td><td class="num">40351</td><td>85043</td><td>DEL</td><td class="num">174.02</td></tr>
              <tr><td>Brightline Parts</td><td>1241785</td><td>9/5/16 13:00</td><td>LT</td><td>CCC</td><td class="num">76155</td><td>85043</td><td>DEL</td><td class="num">142.46</td></tr>
              <tr><td>Brightline Parts</td><td>1241792</td><td>9/5/16 13:00</td><td>LT</td><td>DDD</td><td class="num">76106</td><td>85043</td><td>DEL</td><td class="num">340.47</td></tr>
              <tr><td>Brightline Parts</td><td>1241798</td><td>9/5/16 13:00</td><td>LT</td><td>EEE</td><td class="num">53075</td><td>85043</td><td>DEL</td><td class="num">142.46</td></tr>
              <tr><td>Brightline Parts</td><td>1241813</td><td>9/6/16 13:00</td><td>LT</td><td>FFF</td><td class="num">95361</td><td>85043</td><td>DEL</td><td class="num">155.06</td></tr>
              <tr><td>Brightline Parts</td><td>1241823</td><td>9/6/16 13:00</td><td>LT</td><td>AAA</td><td class="num">7724</td><td>85043</td><td>DEL</td><td class="num">384.73</td></tr>
              <tr><td>Brightline Parts</td><td>1242000</td><td>9/7/16 13:00</td><td>LT</td><td>BBB</td><td class="num">53821</td><td>85043</td><td>DEL</td><td class="num">108.84</td></tr>
              <tr><td>Brightline Parts</td><td>1242005</td><td>9/7/16 13:00</td><td>LT</td><td>CCC</td><td class="num">60148</td><td>85043</td><td>DEL</td><td class="num">154.07</td></tr>
              <tr><td>Brightline Parts</td><td>1242007</td><td>9/7/16 13:00</td><td>LT</td><td>DDD</td><td class="num">37421</td><td>85043</td><td>DEL</td><td class="num">182.44</td></tr>
              <tr><td>Brightline Parts</td><td>1242011</td><td>9/7/16 13:00</td><td>LT</td><td>EEE</td><td class="num">41059</td><td>85043</td><td>DEL</td><td class="num">294.7</td></tr>
              <tr><td>Brightline Parts</td><td>1242471</td><td>9/9/16 13:00</td><td>LT</td><td>FFF</td><td class="num">60502</td><td>85043</td><td>DEL</td><td class="num">132.46</td></tr>
            </tbody>
          </table>
        </div>
        <figcaption class="figure-caption">Figure 3. Lots of data, not much help</figcaption>
      </figure>

      <h2 class="section-heading">Data Must be Processed and Evaluated Properly to be Useful</h2>

      <p>KWRO can help organize, analyze and utilize your data. KWRO arranges for our clients to work based pricing. You get all the benefits of a TMS, plus better rates. You also get custom analysis of your data prepared by KWRO from the information captured and stored in the TMS.</p>

      <p>When your information is exported from the TMS, it comes out in a spreadsheet with no formatting, filtering or meaningful summaries (Fig 3).</p>
    </section>
  </article>
</body>
</html>
```